New Business Card Design Project VORASTI-Italy

we are VORASTI-Italy
our company in the market for 3 years we are luxury cosmetic company and its about time for a facelift :)
i will like to have elegant luxurious and unique business card
that will give the person that get it a unique, luxurious and elegant impression
I'm VERY OPEN FOR NEW IDEAS , even duo i add a few files of things that i see on line and i like them

i add my logo as well
my website is VORASTI.COM
(if you would like to see the main style that we have)

Target Market(s)

adult that have money :)

Industry/Entity Type

Business

Contact Information for Business Card

Name - Paul Vorasti
Position - CEO and CO Founder
address - 4817 E Larkdale
telephone - 555-384-1962
email - paul@vorasti.com
fax - 555-384-1962
website - VORASTI.COM

Colors
000000
959595
fbee3e
ffffff

Requirements
Must have
• big logo in GOLD color
• elegant look
• impressive
Nice to have
• not must but maybe classy pattern background
• not must but maybe emblem
• maybe clear plastic business card
Should not have
• colors
• images

```html
<!DOCTYPE html>
<html lang="en">
<head>
<meta charset="utf-8">
<title>VORASTI Italy — Business Card</title>
<link rel="stylesheet" href="https://fonts.googleapis.com/css2?family=Libre+Baskerville:wght@400;700&family=Arimo:wght@400&display=swap">
<style>
  :root {
    --stage: #1c1c1c;
    --card-top: #3a3a37;
    --card-bottom: #2a2a28;
    --gold: #d9b43a;
    --gold-muted: #a89a6e;
    --deboss: #3b2e1f;
    --deboss-edge: #54432c;
    --text-light: #e4e4e4;
    --text-grey: #959595;
  }
  * { margin: 0; padding: 0; box-sizing: border-box; }
  html, body { width: 1200px; height: 900px; overflow: hidden; }
  body {
    background: var(--stage);
    position: relative;
    font-family: "Arimo", Arial, sans-serif;
  }
  .card {
    position: absolute;
    left: 290px;
    width: 620px;
    height: 354px;
    border-radius: 4px;
    background: linear-gradient(160deg, var(--card-top), var(--card-bottom));
    box-shadow: 0 10px 30px rgba(0,0,0,0.55);
  }
  .card--back { top: 70px; }
  .card--front { top: 476px; }

  /* Back */
  .back-mark {
    position: absolute;
    left: 50%; top: 50%;
    transform: translate(-50%, -50%);
    width: 190px; height: 190px;
    border-radius: 50%;
    border: 3px solid var(--deboss);
    box-shadow: 0 1px 0 var(--deboss-edge);
    display: flex; align-items: center; justify-content: center;
  }
  .back-mark__name {
    font-family: "Libre Baskerville", Georgia, serif;
    font-weight: 700;
    font-size: 24px;
    letter-spacing: 2px;
    color: var(--deboss);
  }

  /* Front: brand block */
  .brand {
    position: absolute;
    left: 40px; top: 46px;
    width: 250px;
    display: flex; flex-direction: column; align-items: center;
  }
  .brand__seal {
    width: 104px; height: 104px;
    border-radius: 50%;
    border: 4px solid var(--gold);
    margin-bottom: 22px;
  }
  .brand__name, .brand__origin {
    font-family: "Libre Baskerville", Georgia, serif;
    font-weight: 700;
    color: var(--gold);
    line-height: 1;
  }
  .brand__name { font-size: 40px; letter-spacing: 1px; }
  .brand__origin { font-size: 15px; letter-spacing: 2px; margin-top: 12px; }

  /* Front: contact block */
  .contact {
    position: absolute;
    left: 340px; top: 48px;
    width: 260px;
  }
  .contact__name {
    font-family: "Libre Baskerville", Georgia, serif;
    font-weight: 700;
    font-size: 22px;
    color: var(--gold-muted);
  }
  .contact__role {
    font-size: 10px;
    color: var(--text-grey);
    margin-top: 6px;
  }
  .contact__list {
    list-style: none;
    margin-top: 26px;
    margin-left: 20px;
  }
  .contact__item {
    display: flex; align-items: flex-start; gap: 12px;
    font-size: 12px;
    line-height: 15px;
    color: var(--text-light);
    margin-bottom: 12px;
  }
  .contact__icon {
    flex: 0 0 12px;
    width: 12px; height: 12px;
    margin-top: 2px;
    fill: var(--text-grey);
  }
</style>
</head>
<body>

  <section class="card card--back" aria-label="Business card, back">
    <div class="back-mark">
      <span class="back-mark__name">VORASTI</span>
    </div>
  </section>

  <section class="card card--front" aria-label="Business card, front">
    <div class="brand">
      <div class="brand__seal"></div>
      <span class="brand__name">VORASTI</span>
      <span class="brand__origin">ITALY</span>
    </div>

    <div class="contact">
      <h1 class="contact__name">Paul Vorasti</h1>
      <p class="contact__role">CEO and CO Founder</p>
      <ul class="contact__list">
        <li class="contact__item">
          <svg class="contact__icon" viewBox="0 0 12 12"><path d="M6 0C3.8 0 2 1.8 2 4c0 3 4 8 4 8s4-5 4-8c0-2.2-1.8-4-4-4zm0 5.5A1.5 1.5 0 1 1 6 2.5a1.5 1.5 0 0 1 0 3z"/></svg>
          <span>4817 E Larkdale<br>Harlow Ridge Nevada 89550</span>
        </li>
        <li class="contact__item">
          <svg class="contact__icon" viewBox="0 0 12 12"><path d="M2.5 0.5l2 2.5-1 1.3c.8 1.6 2 2.8 3.6 3.6l1.3-1 2.6 2-1.2 2.3C5 10.8 1.2 7 .3 2z"/></svg>
          <span>555 384 1962</span>
        </li>
        <li class="contact__item">
          <svg class="contact__icon" viewBox="0 0 12 12"><path d="M0 2h12v8H0z M0 2l6 4.5L12 2" stroke="#2f2f2d" stroke-width="0.8"/></svg>
          <span>paul@vorasti.com</span>
        </li>
        <li class="contact__item">
          <svg class="contact__icon" viewBox="0 0 12 12"><path d="M3 0h6v3H3z M0 4h12v5h-2v3H2V9H0z M3.5 8h5v3h-5z"/></svg>
          <span>555 384 1962</span>
        </li>
        <li class="contact__item">
          <svg class="contact__icon" viewBox="0 0 12 12"><circle cx="6" cy="6" r="6"/><path d="M0 6h12M6 0c-2.5 3-2.5 9 0 12M6 0c2.5 3 2.5 9 0 12" stroke="#2f2f2d" stroke-width="0.8" fill="none"/></svg>
          <span>www.vorasti.com</span>
        </li>
      </ul>
    </div>
  </section>

</body>
</html>
```